BRIM Outreach Partners Business Card Rebrand

Hello Designers! We are looking for help designing our new business card to go in conjunction with our company rebrand. Unfortunately, we have an event mid June that requires we get these printed ASAP (before our new website is launched.) We have a mostly complete Brand Book which I have uploaded to this request for your reference to company information, style, fonts. I've also enclosed our logo file in .eps & .jpg. Attached is a sample business card my boss liked but said was "too simple." I made it in Canva and do not profess to be a designer. NOT FOR DESIGN REFERENCE, ONLY FOR CONTEXT Here is what our old website looks like: https://brimoutreachpartners.com/.

```html
<!DOCTYPE html>
<html lang="en">
<head>
<meta charset="utf-8">
<title>BRIM Outreach Partners – Business Card</title>
<link href="https://fonts.googleapis.com/css2?family=Poppins:wght@400;600;700&family=Open+Sans:wght@400&display=swap" rel="stylesheet">
<style>
  :root {
    --canvas: #d1d2d4;
    --card-dark: #1c1c1c;
    --card-light: #ffffff;
    --accent: #3aa8dc;
    --ink: #141414;
    --ink-soft: #4a4a4a;
    --mark-grey: #cfcfcf;
  }
  * { margin: 0; padding: 0; box-sizing: border-box; }
  html, body { width: 1200px; height: 1000px; overflow: hidden; }
  body { background: var(--canvas); position: relative; font-family: "Poppins", sans-serif; }

  .card { position: absolute; left: 321px; width: 558px; height: 319px; }
  .card-front { top: 162px; background: var(--card-dark); display: flex; align-items: center; justify-content: center; }
  .card-back { top: 519px; background: var(--card-light); }

  .front-brand { display: flex; align-items: center; gap: 16px; }
  .brand-dot { width: 78px; height: 78px; border-radius: 50%; background: var(--accent); flex: none; }
  .front-name { font-family: "Poppins", sans-serif; font-weight: 600; font-size: 27px; color: var(--mark-grey); letter-spacing: 0.5px; }

  .back-band { position: absolute; left: 0; top: 0; width: 174px; height: 319px; background: var(--card-dark); border-right: 3px solid var(--accent); }
  .band-name {
    position: absolute; left: 50%; top: 50%;
    transform: translate(-50%, -50%) rotate(-90deg);
    white-space: nowrap;
    font-family: "Poppins", sans-serif; font-weight: 700; font-size: 23px;
    color: #ffffff; letter-spacing: 0.5px;
  }

  .back-details { position: absolute; left: 209px; top: 74px; }
  .person-name { font-weight: 600; font-size: 17px; color: var(--ink); line-height: 24px; }
  .person-title { font-family: "Open Sans", sans-serif; font-size: 15px; color: var(--accent); line-height: 20px; }
  .location { margin-top: 43px; font-size: 13px; color: var(--ink-soft); line-height: 18px; padding-left: 2px; }
  .contact-list { list-style: none; margin-top: 7px; }
  .contact-list li { display: flex; align-items: center; gap: 6px; font-size: 13px; color: var(--ink-soft); line-height: 17px; }
  .contact-list svg { width: 13px; height: 13px; flex: none; }

  .back-dot { position: absolute; left: 465px; top: 233px; width: 56px; height: 56px; border-radius: 50%; background: var(--accent); }
</style>
</head>
<body>
  <section class="card card-front">
    <div class="front-brand">
      <span class="brand-dot"></span>
      <span class="front-name">BRIM Outreach Partners</span>
    </div>
  </section>

  <section class="card card-back">
    <div class="back-band">
      <span class="band-name">BRIM Outreach Partners</span>
    </div>

    <div class="back-details">
      <p class="person-name">Jordan Vale-Morris</p>
      <p class="person-title">Managing Partner</p>
      <p class="location">Atlanta, Ga based (Central Time)</p>
      <ul class="contact-list">
        <li>
          <svg viewBox="0 0 16 16" aria-hidden="true"><path fill="#3aa8dc" d="M3 2h3l1.5 3.5-2 1.2a8 8 0 0 0 3.8 3.8l1.2-2L14 10v3a1 1 0 0 1-1 1A11 11 0 0 1 2 3a1 1 0 0 1 1-1z"/></svg>
          555-214-7390
        </li>
        <li>
          <svg viewBox="0 0 16 16" aria-hidden="true"><rect x="1" y="3" width="14" height="10" rx="1" fill="#3aa8dc"/><path d="M1.5 3.5 8 8.5l6.5-5" fill="none" stroke="#fff" stroke-width="1.2"/></svg>
          Jordan@brimoutreachpartners.com
        </li>
        <li>
          <svg viewBox="0 0 16 16" aria-hidden="true"><circle cx="8" cy="8" r="7" fill="#3aa8dc"/><path d="M1 8h14M8 1c-2.5 2-2.5 12 0 14M8 1c2.5 2 2.5 12 0 14" fill="none" stroke="#fff" stroke-width="1"/></svg>
          www.brimoutreachpartners.com
        </li>
      </ul>
    </div>

    <span class="back-dot"></span>
  </section>
</body>
</html>
```